Modern & Aesthetic Electrician Sign Design for Work Vehicle

Modern and aesthetic signage design for an electricians work vehicle. Including already designed logo, mobile number, ABN, licensing number and services offered. Preference is black background, symmetric design with logo centred, services offered at bottom of sign in smaller size font. Mobile number readable and big enough to standout without being too large.

Industry/Entity Type

Electrician

Font styles to use
Serif
Sans Serif

Colors
000000
ffffff
ec1f27

Requirements
Must have
• Logo
• Services Offered
• Mobile Number
• ABN
• License Number
• Black background

```html
<!DOCTYPE html>
<html lang="en">
<head>
<meta charset="utf-8">
<title>Volta Electrical – Vehicle Sign</title>
<link rel="stylesheet" href="https://fonts.googleapis.com/css2?family=Michroma&family=Arimo:wght@400;700&display=swap">
<style>
  :root {
    --sign-black: #000000;
    --sign-white: #ffffff;
    --sign-red: #ec1f27;
  }
  * { margin: 0; padding: 0; box-sizing: border-box; }
  html, body {
    width: 1200px;
    height: 402px;
    overflow: hidden;
    background: var(--sign-white);
  }
  .vehicle-sign {
    position: relative;
    width: 1200px;
    height: 402px;
    background: var(--sign-white);
  }
  .sign-panel {
    position: absolute;
    left: 42px;
    top: 42px;
    width: 1118px;
    height: 316px;
    background: var(--sign-black);
  }
  .brand-circle {
    position: absolute;
    left: 118px;
    top: 104px;
    width: 240px;
    height: 240px;
  }
  .brand-name {
    position: absolute;
    left: 436px;
    top: 78px;
    font-family: "Michroma", sans-serif;
    font-weight: 400;
    color: var(--sign-red);
    line-height: 1;
  }
  .brand-name__main {
    display: block;
    font-size: 104px;
    letter-spacing: 4px;
  }
  .brand-name__trade {
    display: block;
    margin-top: 16px;
    font-size: 36px;
    letter-spacing: 22px;
  }
  .service-details {
    position: absolute;
    left: 438px;
    top: 266px;
    font-family: "Arimo", sans-serif;
    font-weight: 400;
    font-size: 28px;
    line-height: 36px;
    color: var(--sign-white);
  }
  .phone-band {
    position: absolute;
    left: 1090px;
    top: 42px;
    width: 70px;
    height: 316px;
    background: var(--sign-red);
    display: flex;
    justify-content: center;
    align-items: center;
  }
  .phone-band__label {
    writing-mode: vertical-rl;
    text-orientation: upright;
    font-family: "Arimo", sans-serif;
    font-weight: 700;
    font-size: 25px;
    letter-spacing: 7px;
    color: var(--sign-white);
  }
</style>
</head>
<body>
  <main class="vehicle-sign">
    <div class="sign-panel"></div>

    <svg class="brand-circle" viewBox="0 0 240 240" aria-hidden="true">
      <circle cx="120" cy="120" r="113" fill="none" stroke="var(--sign-white)" stroke-width="12"/>
    </svg>

    <h1 class="brand-name">
      <span class="brand-name__main">VOLTA</span>
      <span class="brand-name__trade">ELECTRICAL</span>
    </h1>

    <div class="service-details">
      <p class="service-details__services">SERVICE OFFERED - SERVICE OFFERED</p>
      <p class="service-details__license">LICENSE NUMBER</p>
    </div>

    <div class="phone-band">
      <span class="phone-band__label">TELEPHONE</span>
    </div>
  </main>
</body>
</html>
```